Clean and sophisticated website for Darulnoor

Darulnoor is a group of enthusiasts offering education, welfare, health and publications. The organization is going through a re branding phase and looking to design a new website for darulnoor.org. The current landing page will be replaced by the new website. Looking for a creative design that could be converted into a responsive wordpress theme and integrated on the website.

The new website will have all the content of the 4 different sites that are accessible from the landing page.

Target Market(s)

Donors, information seekers, and students.

Industry/Entity Type

Non-Profit

Number of Pages Required

5+ page

Font styles to use
Sans Serif

Requirements
Must have
• Sophisticated look.
• Multi lingual interface (English + Urdu)
• Great User experience and Easy Navigation
• SEO friendly
• Prominent sections for 4 main categories
• Responsive design
Nice to have
• banners
• Parallax
• Call to action buttons
• simple clean design
Should not have
• Dark Colors
• Busy portal style look
• Flash
• cluttered design

```html
<!DOCTYPE html>
<html lang="en">
<head>
<meta charset="utf-8">
<title>Darulnoor</title>
<link href="https://fonts.googleapis.com/css2?family=Lato:wght@400;700;900&family=Open+Sans:wght@400;600&display=swap" rel="stylesheet">
<style>
:root{
  --blue:#1b6fc0;
  --blue-dark:#175fa6;
  --orange:#f0622e;
  --ink:#3c3c3c;
  --muted:#777;
  --line:#e3e3e3;
  --soft:#f4f4f4;
  --white:#fff;
}
*{margin:0;padding:0;box-sizing:border-box}
html,body{width:1200px;height:2695px;overflow:hidden}
body{position:relative;background:var(--white);font-family:"Open Sans",Arial,sans-serif;color:var(--ink)}
.abs{position:absolute}
.btn{position:absolute;display:flex;align-items:center;justify-content:center;background:var(--blue);color:var(--white);font-family:"Open Sans",Arial,sans-serif;font-size:12px;border-radius:3px;box-shadow:0 2px 0 var(--blue-dark)}
.heading{font-family:"Lato",Arial,sans-serif;font-weight:700;color:var(--blue);text-transform:uppercase}

/* header */
.site-header{position:absolute;left:0;top:0;width:1200px;height:108px;background:var(--white);border-top:3px solid var(--blue);z-index:3}
.nav-item{position:absolute;top:46px;font-family:"Lato",Arial,sans-serif;font-size:12px;color:#555;text-transform:uppercase;letter-spacing:.3px}
.nav-item.active{color:var(--blue)}
.nav-underline{position:absolute;left:187px;top:101px;width:40px;height:4px;background:var(--blue)}
.lang{position:absolute;left:997px;top:42px;width:73px;height:26px;border:1px solid #ddd;border-radius:2px;font-size:10px;color:#444;display:flex;align-items:center;justify-content:center;gap:5px}
.lang .flag{width:12px;height:8px;background:linear-gradient(#c8102e 0 33%,#fff 33% 66%,#1f3d8a 66%)}
.brand{position:absolute;left:526px;top:0;width:148px;height:278px;z-index:4}
.brand-name{position:absolute;left:0;top:140px;width:148px;text-align:center;font-family:"Lato",Arial,sans-serif;font-weight:900;font-size:19px;color:var(--blue);letter-spacing:.5px}

/* hero */
.hero{position:absolute;left:0;top:108px;width:1200px;height:467px;background:linear-gradient(90deg,#f3f3f3 0%,#eeeeee 35%,#d9d6d2 60%,#c9b7a5 78%,#e5e2de 100%)}
.hero-title{position:absolute;left:131px;top:118px;font-size:50px;letter-spacing:.5px}
.hero-text{position:absolute;left:131px;top:198px;width:340px;font-size:12.5px;line-height:24px;color:#555}
.dots{position:absolute;left:133px;top:347px;display:flex;gap:7px}
.dots span{width:10px;height:10px;border-radius:50%;background:#c9c9c9}
.dots span:first-child{background:var(--blue)}

/* welcome */
.welcome-title{position:absolute;left:131px;top:645px;font-size:36px}
.body-text{font-size:11.5px;line-height:24px;color:#555}
.video{position:absolute;left:625px;top:654px;width:444px;height:294px;border:1px solid #ddd;padding:4px;background:var(--white)}
.video-fill{width:100%;height:100%;background:linear-gradient(120deg,#e9eef2 0%,#c9d6df 40%,#8a7aa8 55%,#dfe6ea 80%)}
.play{position:absolute;left:196px;top:128px;width:56px;height:38px;background:rgba(80,80,80,.7);border-radius:3px}

/* services */
.services{position:absolute;left:0;top:1042px;width:1200px;height:641px;background:var(--soft)}
.section-title{position:absolute;left:0;width:1200px;text-align:center;font-size:33px}
.service{position:absolute;top:171px;width:218px;height:373px}
.service svg.card{position:absolute;left:0;top:0}
.service .icon{position:absolute;left:46px;top:17px;width:126px;height:126px;border-radius:50%;background:var(--blue);display:flex;align-items:center;justify-content:center}
.service .icon.orange{background:var(--orange)}
.service h3{position:absolute;left:0;top:166px;width:218px;text-align:center;font-size:20px}
.service p{position:absolute;left:22px;top:206px;width:174px;text-align:center;font-size:10.5px;line-height:24px;color:#555}
.service .btn{left:68px;top:302px;width:82px;height:26px;font-size:11px}

/* blog */
.post{position:absolute;top:1832px;width:298px;height:460px;border:1px solid var(--line);background:var(--white)}
.post-img{height:221px}
.post .date{position:absolute;left:18px;top:258px;font-size:11px;color:#333}
.post h3{position:absolute;left:18px;top:288px;font-size:20px}
.post p{position:absolute;left:18px;top:326px;width:262px;font-size:10.5px;line-height:20px;color:#999}
.post .btn{left:16px;top:416px;width:82px;height:27px;font-size:11px}

/* footer */
.site-footer{position:absolute;left:0;top:2368px;width:1200px;height:327px;background:var(--soft)}
.foot-brand{position:absolute;left:126px;top:120px;font-family:"Lato",Arial,sans-serif;font-weight:900;font-size:26px;color:var(--blue);letter-spacing:.5px}
.foot-title{position:absolute;top:50px;font-size:15px}
.links{position:absolute;left:376px;top:88px;list-style:none}
.links li{font-size:10.5px;line-height:24px;color:#666;text-transform:uppercase}
.news-text{position:absolute;left:564px;top:90px;width:240px;font-size:11px;line-height:24px;color:#555}
.email{position:absolute;left:562px;top:151px;width:237px;height:34px;border:1px solid #ccc;background:var(--white);font-size:11px;color:#555;padding:9px 10px}
.subscribe{left:562px;top:204px;width:99px;height:29px;font-size:10.5px}
.contact{position:absolute;left:900px;top:92px;list-style:none}
.contact li{display:flex;align-items:flex-start;gap:12px;font-size:11px;color:#555;height:28px;line-height:14px}
.contact li svg{flex:none;margin-top:1px}
.contact a{color:#555}
.footer-rule{position:absolute;left:0;top:273px;width:1200px;height:1px;background:#ddd}
.copyright{position:absolute;left:0;top:291px;width:1200px;text-align:center;font-size:10.5px;color:#777}
</style>
</head>
<body>

<header class="site-header">
  <nav>
    <span class="nav-item active" style="left:189px">Home</span>
    <span class="nav-item" style="left:275px">About</span>
    <span class="nav-item" style="left:363px">Publications</span>
    <span class="nav-item" style="left:700px">Welfare</span>
    <span class="nav-item" style="left:803px">Education</span>
    <span class="nav-item" style="left:918px">Bayanat</span>
  </nav>
  <div class="nav-underline"></div>
  <div class="lang"><span class="flag"></span>ENG <span style="font-size:8px">&#9662;</span></div>
</header>

<div class="brand">
  <svg width="148" height="278" viewBox="0 0 148 278">
    <polygon points="0,0 148,0 148,208 74,278 0,208" fill="#fff"/>
  </svg>
  <div class="brand-name">DARULNOOR</div>
</div>

<section class="hero" role="img" aria-label="Banner photo of a smiling student holding books in a classroom">
  <h1 class="heading hero-title">Publications</h1>
  <p class="hero-text">Nemo enim ipsam voluptatem quia voluptas sit aspernatur aut odit aut fugit, sed quia consequuntur</p>
  <span class="btn" style="left:131px;top:278px;width:117px;height:36px">Read More</span>
  <div class="dots"><span></span><span></span><span></span><span></span></div>
</section>

<section class="welcome">
  <h2 class="heading welcome-title">Welcome to Darulnoor</h2>
  <p class="abs body-text" style="left:133px;top:714px;width:462px">Nemo enim ipsam voluptatem quia voluptas sit aspernatur aut odit aut fugit, sed quia consequuntur</p>
  <p class="abs body-text" style="left:133px;top:786px;width:462px">Neque porro quisquam est, qui dolorem ipsum quia dolor sit amet, consectetur, adipisci velit, sed quia non numquam eius modi tempora incidunt ut labore et dolore magnam aliquam quaerat voluptatem. Ut enim ad minima veniam, quis nostrum exercitationem ullam corporis suscipit laboriosam, nisi ut aliquid ex ea commodi consequatur</p>
  <span class="btn" style="left:133px;top:913px;width:117px;height:35px">Read More</span>
  <div class="video">
    <div class="video-fill" role="img" aria-label="Video still of a student choosing a book in a library"></div>
    <svg class="play" viewBox="0 0 56 38"><polygon points="22,10 22,28 36,19" fill="#fff"/></svg>
  </div>
</section>

<section class="services">
  <h2 class="heading section-title" style="top:73px">Our Services</h2>

  <div class="service" style="left:129px">
    <svg class="card" width="218" height="373"><polygon points="1,1 217,1 217,332 109,372 1,332" fill="#fff" stroke="#e2e2e2"/></svg>
    <div class="icon orange"><svg width="44" height="52" viewBox="0 0 44 52" fill="none" stroke="#fff" stroke-width="4" stroke-linecap="round"><rect x="14" y="2" width="16" height="28" rx="8" fill="#fff"/><path d="M6 22a16 16 0 0 0 32 0M22 38v10M14 48h16"/></svg></div>
    <h3 class="heading">Bayanat</h3>
    <p>Nemo enim ipsam voluptatem quia voluptas sit aspernatur aut odit aut fugit, sed quia consequuntur</p>
    <span class="btn">Read More</span>
  </div>

  <div class="service" style="left:372px">
    <svg class="card" width="218" height="373"><polygon points="1,1 217,1 217,332 109,372 1,332" fill="#fff" stroke="#e2e2e2"/></svg>
    <div class="icon"><svg width="54" height="46" viewBox="0 0 54 46"><path d="M19 8V3h16v5" fill="none" stroke="#fff" stroke-width="4"/><rect x="2" y="8" width="50" height="36" rx="4" fill="#fff"/><path d="M27 16v20M17 26h20" stroke="var(--blue)" stroke-width="7"/></svg></div>
    <h3 class="heading">Welfare</h3>
    <p>Nemo enim ipsam voluptatem quia voluptas sit aspernatur aut odit aut fugit, sed quia consequuntur</p>
    <span class="btn">Read More</span>
  </div>

  <div class="service" style="left:613px">
    <svg class="card" width="218" height="373"><polygon points="1,1 217,1 217,332 109,372 1,332" fill="#fff" stroke="#e2e2e2"/></svg>
    <div class="icon"><svg width="56" height="48" viewBox="0 0 56 48" fill="#fff"><path d="M4 16h10l26-12v40L14 32H4z"/><path d="M12 32l5 14h7l-4-14z"/><path d="M46 16q6 8 0 16" fill="none" stroke="#fff" stroke-width="4" stroke-linecap="round"/></svg></div>
    <h3 class="heading">Publications</h3>
    <p>Nemo enim ipsam voluptatem quia voluptas sit aspernatur aut odit aut fugit, sed quia consequuntur</p>
    <span class="btn">Read More</span>
  </div>

  <div class="service" style="left:851px">
    <svg class="card" width="218" height="373"><polygon points="1,1 217,1 217,332 109,372 1,332" fill="#fff" stroke="#e2e2e2"/></svg>
    <div class="icon"><svg width="50" height="52" viewBox="0 0 50 52"><path d="M14 2h34l-8 38H6z" fill="#fff"/><path d="M6 40h34l-2 10H4z" fill="#fff"/><path d="M6 40q-4 5 0 10" fill="none" stroke="#fff" stroke-width="3"/><path d="M18 12h20M16 20h20" stroke="var(--blue)" stroke-width="3"/></svg></div>
    <h3 class="heading">Education</h3>
    <p>Nemo enim ipsam voluptatem quia voluptas sit aspernatur aut odit aut fugit, sed quia consequuntur</p>
    <span class="btn">Read More</span>
  </div>
</section>

<section class="blog">
  <h2 class="heading section-title" style="top:1754px">Recent Blog</h2>

  <article class="post" style="left:131px">
    <div class="post-img" role="img" aria-label="Photo of a student reading a book in a library" style="background:linear-gradient(120deg,#eef3f4 0%,#d8e4e6 40%,#3fb2b4 62%,#e8eef0 100%)"></div>
    <span class="date">DEC 16,2016</span>
    <h3 class="heading">Intellect Magazine</h3>
    <p>Nemo enim ipsam voluptatem quia voluptas sit aspernatur aut odit aut fugit, sed quia consequuntur magni dolores eos qui ratione voluptatem.</p>
    <span class="btn">Read More</span>
  </article>

  <article class="post" style="left:451px">
    <div class="post-img" role="img" aria-label="Photo of students at computers in a classroom" style="background:linear-gradient(120deg,#dfe8c8 0%,#b9c9a0 35%,#5d6b7c 55%,#e2e0cf 100%)"></div>
    <span class="date">DEC 16,2016</span>
    <h3 class="heading">Intellect Magazine</h3>
    <p>Nemo enim ipsam voluptatem quia voluptas sit aspernatur aut odit aut fugit, sed quia consequuntur magni dolores eos qui ratione voluptatem.</p>
    <span class="btn">Read More</span>
  </article>

  <article class="post" style="left:771px">
    <div class="post-img" role="img" aria-label="Photo of library bookshelves" style="background:linear-gradient(100deg,#e8d7b8 0%,#b48a5a 35%,#6a4a36 60%,#8c6b4a 100%)"></div>
    <span class="date">DEC 16,2016</span>
    <h3 class="heading">Intellect Magazine</h3>
    <p>Nemo enim ipsam voluptatem quia voluptas sit aspernatur aut odit aut fugit, sed quia consequuntur magni dolores eos qui ratione voluptatem.</p>
    <span class="btn">Read More</span>
  </article>
</section>

<footer class="site-footer">
  <div class="foot-brand">DARULNOOR</div>

  <h4 class="heading foot-title" style="left:374px">Quick Links</h4>
  <ul class="links">
    <li>Home</li><li>About</li><li>Publications</li><li>Welfare</li><li>Education</li><li>Bayanat</li>
  </ul>

  <h4 class="heading foot-title" style="left:564px">Newsletter</h4>
  <p class="news-text">Enter your email address to receive the latest news our blog.</p>
  <div class="email">Email id</div>
  <span class="btn subscribe">SUBSCRIBE</span>

  <h4 class="heading foot-title" style="left:898px">Contact Us</h4>
  <ul class="contact">
    <li><svg width="13" height="13" viewBox="0 0 13 13" fill="#555"><path d="M1 4q0-3 3-3h5q3 0 3 3v1H9V3H4v2H1z"/><rect x="2" y="6" width="9" height="6" rx="1"/></svg>(555) 014-2300</li>
    <li><svg width="13" height="13" viewBox="0 0 13 13" fill="#555"><rect x="3" y="1" width="7" height="4"/><rect x="1" y="5" width="11" height="5" rx="1"/><rect x="3" y="8" width="7" height="4" fill="#fff" stroke="#555"/></svg>(555) 014-2300</li>
    <li><svg width="13" height="13" viewBox="0 0 13 13"><rect x="1" y="3" width="11" height="8" fill="#555"/><path d="M1 3l5.5 4L12 3" fill="none" stroke="#fff"/></svg><a>info@darulnoor.org</a></li>
    <li><svg width="13" height="13" viewBox="0 0 13 13" fill="#555"><path d="M6.5 0a4 4 0 0 1 4 4c0 3-4 9-4 9s-4-6-4-9a4 4 0 0 1 4-4z"/><circle cx="6.5" cy="4" r="1.5" fill="#fff"/></svg><span># 2868 Lorem ipsum dolor sit<br>amet, consectetur</span></li>
  </ul>

  <div class="footer-rule"></div>
  <p class="copyright">&copy;2016darulnoor.org. All rights reserved.</p>
</footer>

</body>
</html>
```